Veridane Works, Inc. - Update our Website

Veridane Works needs a website to help our customers to navigate through our services efficiently. Our existing website is at www.verowk.example

We would like to explain our services with content and pictures (photographs) that distinguishes our products and services from our competition.

The website design must implement a strategy to focus on our Contract Labeling services.

With this new design we would like to attract new customers and ensure that our existing customers are fully informed with our latest offerings.

```html
<!DOCTYPE html>
<html lang="en">
<head>
<meta charset="utf-8">
<title>Veridane Works, Inc.</title>
<link rel="stylesheet" href="https://fonts.googleapis.com/css2?family=Roboto:wght@300;400;500;700&display=swap">
<style>
:root{
  --blue:#1a87c4;
  --green:#6cc417;
  --orange:#f7890c;
  --charcoal:#3a3a3a;
  --text:#444;
  --muted:#8a8a8a;
  --line:#e2e2e2;
  --footer:#2f2f2f;
  --footer-base:#262626;
  --footer-text:#9a9a9a;
  --white:#fff;
}
*{box-sizing:border-box;margin:0;padding:0}
html,body{width:1200px;height:2308px;overflow:hidden;background:var(--white)}
body{position:relative;font-family:'Roboto',Arial,sans-serif;color:var(--text)}
.abs{position:absolute}

/* header */
.brand{left:57px;top:44px;display:flex;align-items:center;gap:12px}
.brand-dot{width:40px;height:40px;border-radius:50%;background:var(--blue)}
.brand-name{font-size:25px;font-weight:700;color:#333;letter-spacing:.5px}
.contact-line{top:26px;font-size:13px;color:#777;display:flex;align-items:center;gap:8px}
.contact-line svg{fill:var(--blue)}
.social{left:990px;top:57px;display:flex;gap:0}
.social span{width:31px;height:31px;border:1px solid #ddd;display:block;position:relative}
.social span::after{content:"";position:absolute;left:11px;top:11px;width:8px;height:8px;background:#c8c8c8}

.nav{left:57px;top:120px;width:1086px;height:50px;border:1px solid var(--line);display:flex}
.nav a{font-size:13px;color:#555;text-decoration:none;display:flex;align-items:center;justify-content:center;border-right:1px solid var(--line);text-transform:uppercase}
.nav a.active{background:var(--blue);color:var(--white)}
.nav-search{position:absolute;right:-1px;top:-1px;width:50px;height:50px;background:var(--blue);display:flex;align-items:center;justify-content:center}

/* hero */
.hero{left:0;top:199px;width:1200px;height:567px;background:linear-gradient(100deg,#f4f3f1 0%,#e9e3dc 35%,#d9b9a2 60%,#c99a80 75%,#eef0f2 100%)}
.hero-card{left:59px;top:252px;width:466px;height:184px;background:rgba(255,255,255,.72);padding:24px 30px}
.hero-card h1{font-weight:300;font-size:31px;color:#444;line-height:1.1}
.hero-card h1 em{display:block;font-style:normal;color:var(--blue);font-size:46px}
.hero-card p{margin-top:22px;font-size:14px;color:#9a9a9a;line-height:1.45}

/* feature tiles */
.tiles{left:57px;top:594px;width:1086px;height:252px;display:flex}
.tile{flex:1;color:var(--white);padding:22px 26px;position:relative}
.tile h2{font-weight:300;font-size:29px;line-height:1.05;height:70px}
.tile p{font-size:12px;line-height:1.55}
.tile .more{position:absolute;left:26px;top:200px;font-size:13px}
.tile.serv{background:var(--blue)}
.tile.book{background:var(--green)}
.tile.rand{background:var(--orange)}
.tile.hours{background:var(--charcoal)}
.hours table{width:100%;border-collapse:collapse;font-size:12px;margin-top:-8px}
.hours td{padding:12px 0;border-bottom:1px solid #555}
.hours td:last-child{text-align:right}
.hours tr:last-child td{border-bottom:0}

/* welcome */
.welcome{left:0;top:890px;width:1200px;text-align:center}
.welcome h2{font-weight:300;font-size:36px;color:var(--blue)}
.welcome h2 strong{font-weight:500}
.welcome p{margin-top:14px;font-size:18px;font-weight:300;color:#777;line-height:1.4}

.services{left:57px;top:1062px;width:1086px;display:flex}
.service{width:25%;text-align:center;padding:0 14px}
.service svg{display:block;margin:0 auto;height:56px}
.service h3{margin-top:14px;font-weight:400;font-size:20px;color:#333}
.service p{margin-top:10px;font-size:12.5px;color:var(--muted);line-height:1.45}

.divider{left:57px;top:1292px;width:1086px;height:1px;background:var(--line)}
.divider::before{content:"";position:absolute;left:0;top:-1px;width:235px;height:3px;background:var(--blue)}

/* news + testimonials */
.section-title{top:1355px;font-size:20px;font-weight:400;color:#333}
.section-rule{top:1397px;height:1px;background:var(--line)}
.pager{display:flex;gap:2px}
.pager span{width:23px;height:23px;border:1px solid #ddd;display:flex;align-items:center;justify-content:center}
.pager span.on{background:var(--blue);border-color:var(--blue)}

.news-thumb{left:57px;width:123px;height:122px}
.thumb-spa{background:linear-gradient(135deg,#f3dccb,#e8c2a6 55%,#f6ece4)}
.thumb-device{background:linear-gradient(135deg,#e6e9ec,#b9c0c6 55%,#f2f3f4)}
.news-item{left:208px;width:370px}
.news-item h3{font-weight:400;font-size:20px;color:var(--blue)}
.news-item .meta{margin-top:4px;font-size:11px;color:var(--muted)}
.news-item .meta b{font-weight:400;color:var(--blue)}
.news-item p{margin-top:10px;font-size:12.5px;color:#777;line-height:1.45}

.quote-box{left:621px;top:1446px;width:522px;height:170px;border:1px solid #ddd}
.quote-box::after{content:"";position:absolute;left:30px;bottom:-12px;width:20px;height:20px;background:var(--white);border-right:1px solid #ddd;border-bottom:1px solid #ddd;transform:rotate(45deg)}
.qmark{width:33px;height:33px;background:var(--blue);color:var(--white);font-size:34px;font-weight:700;line-height:44px;text-align:center}
.quote-text{left:700px;top:1476px;width:400px;font-size:13px;color:#888;line-height:1.65}
.avatar{left:621px;top:1647px;width:55px;height:57px;background:#dcdcdc}
.person{left:700px;top:1666px}
.person b{display:block;font-weight:400;font-size:14px;color:#333}
.person span{font-size:11px;color:var(--blue)}

/* update strip */
.strip{left:0;top:1773px;width:1200px;height:59px;background:var(--blue);display:flex;align-items:center;padding-left:57px;color:var(--white)}
.strip-mark{width:22px;height:22px;border-radius:50%;background:var(--white);margin-right:40px}
.strip p{font-size:13px}
.strip .pager{position:absolute;right:57px}
.strip .pager span{border-color:rgba(255,255,255,.8)}

/* footer */
.footer{left:0;top:1832px;width:1200px;height:423px;background:var(--footer)}
.footer-base{left:0;top:2255px;width:1200px;height:53px;background:var(--footer-base);font-size:11px;color:#777;padding:22px 57px}
.fcol{top:1868px;color:var(--footer-text);font-size:12.5px}
.fcol h4{font-weight:400;font-size:18px;color:var(--white)}
.fcol h4::after{content:"";display:block;width:42px;height:2px;background:var(--blue);margin-top:9px}
.fcol p{line-height:1.5}
.finfo{display:flex;gap:16px;align-items:flex-start;margin-top:20px;color:#ccc;font-size:12px;line-height:1.6}
.finfo svg{flex:none;fill:var(--blue);margin-top:2px}
.fcol ul{list-style:none;margin-top:33px}
.fcol li{font-size:12px;color:#ddd;height:33px;display:flex;gap:12px}
.fcol li::before{content:"›";color:#888}
.field-label{font-size:12px;color:#bbb;margin-top:14px}
.field{margin-top:8px;border:1px solid #555;background:#2a2a2a;width:243px}
.btn{margin-top:22px;width:82px;height:34px;background:var(--white);color:#333;font-size:12px;display:flex;align-items:center;justify-content:center}
.footer-photo{left:338px;top:1947px;width:243px;height:145px;background:linear-gradient(120deg,#dbe6ee,#f4f6f8 45%,#c9d6e0)}
</style>
</head>
<body>

<header>
  <div class="abs brand"><span class="brand-dot"></span><span class="brand-name">VERIDANE WORKS</span></div>
  <div class="abs contact-line" style="left:832px">
    <svg width="12" height="14" viewBox="0 0 12 14"><rect x="2" y="0" width="8" height="14" rx="1.5"/></svg>Call us: 1-800-555-0147
  </div>
  <div class="abs contact-line" style="left:1003px">
    <svg width="14" height="11" viewBox="0 0 14 11"><rect width="14" height="11" rx="1"/></svg>contact@veridane.example
  </div>
  <div class="abs social" aria-label="Social links"><span></span><span></span><span></span><span></span><span></span></div>

  <nav class="abs nav">
    <a class="active" href="#" style="width:119px">Home</a>
    <a href="#" style="width:122px">About us</a>
    <a href="#" style="width:136px">User support</a>
    <a href="#" style="width:122px">Contacts</a>
    <span class="nav-search"><svg width="18" height="18" viewBox="0 0 18 18" fill="none" stroke="#fff" stroke-width="2.6"><circle cx="7.5" cy="7.5" r="5.5"/><path d="M11.5 11.5l5 5"/></svg></span>
  </nav>
</header>

<section>
  <div class="abs hero" role="img" aria-label="Photograph of a caregiver's hand gently holding an elderly patient's hand"></div>
  <div class="abs hero-card">
    <h1>We Care About<em>Every Client</em></h1>
    <p>Cum sociis natoque penatibus et magnis dis parturient montesmus. Pro vel nibh et elit mollis commodo et nec augue tristique sed.</p>
  </div>

  <div class="abs tiles">
    <div class="tile serv"><h2>VeriServ™</h2><p>VeriServ™ is a contract clinical label generation service that provides you with ready to apply clinical labels specifically...</p><span class="more">Read More</span></div>
    <div class="tile book"><h2>VeriBook™</h2><p>VeriBook™ labels are multi-page clinical labels used to address the needs of multi-language studies. This enables user to prepare...</p><span class="more">Read More</span></div>
    <div class="tile rand"><h2>Clinical Randomizations</h2><p>Our systems can create randomization data for all types of CTM requirements. Patient randomization, material randomization and random...</p><span class="more">Read More</span></div>
    <div class="tile hours"><h2>Opening Hours</h2>
      <table>
        <tr><td>Monday - Friday</td><td>8.00 - 17.00</td></tr>
        <tr><td>Saturday</td><td>9.30 - 17.30</td></tr>
        <tr><td>Sunday</td><td>9.30 - 15.00</td></tr>
      </table>
    </div>
  </div>
</section>

<section>
  <div class="abs welcome">
    <h2>Welcome to <strong>Veridane Works.inc</strong></h2>
    <p>Veridane Works, Inc. specializes in providing products and services to the pharmaceutical industry.<br>We are focused on the needs of those individuals involved with Clinical Trial Materials.<br>Our products and services are summarized below:</p>
  </div>

  <div class="abs services">
    <div class="service">
      <svg viewBox="0 0 56 50" width="56"><path d="M28 46C10 33 3 24 3 15 3 8 8 3 15 3c6 0 10 4 13 8 3-4 7-8 13-8 7 0 12 5 12 12 0 9-7 18-25 31z" fill="none" stroke="#1a87c4" stroke-width="4"/><path d="M6 24h13l4-8 6 16 5-10h16" fill="none" stroke="#1a87c4" stroke-width="3.5"/></svg>
      <h3>VeriPro/LBL™</h3>
      <p>Cum sociis natoque penatibus et magnis dis parturient montesmus. Pro vel nibh et elit mollis commodo et nec augueque</p>
    </div>
    <div class="service">
      <svg viewBox="0 0 56 50" width="56"><g transform="rotate(-45 28 25)"><rect x="8" y="16" width="40" height="18" rx="9" fill="none" stroke="#1a87c4" stroke-width="4"/><path d="M28 16v18" stroke="#1a87c4" stroke-width="4"/><path d="M15 25h8" stroke="#1a87c4" stroke-width="3"/></g></svg>
      <h3>Software Validation Services</h3>
      <p>Cum sociis natoque penatibus et magnis dis parturient montesmus. Pro vel nibh et elit mollis commodo et nec augueque</p>
    </div>
    <div class="service">
      <svg viewBox="0 0 56 50" width="56"><rect x="18" y="4" width="20" height="10" rx="2" fill="none" stroke="#f7890c" stroke-width="4"/><rect x="4" y="12" width="48" height="34" rx="4" fill="#f7890c"/><circle cx="28" cy="29" r="11" fill="#fff"/><path d="M28 22v14M21 29h14" stroke="#f7890c" stroke-width="4"/></svg>
      <h3>Clinical Label Stock</h3>
      <p>Cum sociis natoque penatibus et magnis dis parturient montesmus. Pro vel nibh et elit mollis commodo et nec augueque</p>
    </div>
    <div class="service">
      <svg viewBox="0 0 56 56" width="50"><path d="M16 54V40C9 35 6 28 7 20 9 9 18 3 29 3c12 0 20 8 20 19l5 10h-5v8c0 3-2 5-5 5h-6v9z" fill="#1a87c4"/><circle cx="29" cy="20" r="7" fill="#fff"/></svg>
      <h3>Qualified Doctors</h3>
      <p>Cum sociis natoque penatibus et magnis dis parturient montesmus. Pro vel nibh et elit mollis commodo et nec augueque</p>
    </div>
  </div>
  <div class="abs divider"></div>
</section>

<section>
  <h2 class="abs section-title" style="left:57px">Latest News</h2>
  <div class="abs section-rule" style="left:57px;width:522px"></div>

  <div class="abs news-thumb thumb-spa" style="top:1441px" role="img" aria-label="Photograph of a young woman receiving a neck treatment"></div>
  <div class="abs news-item" style="top:1448px">
    <h3>Young women having her neck pain checked</h3>
    <div class="meta">September 15, 2013 &nbsp; <b>Comments (4)</b></div>
    <p>Cum sociis natoque penatibus et magnis dis parturient montesmus. Pro vel nibh et elit mollis commodo et nec augueique Mauris at justo eu lectus auctor porta vel ut libero.</p>
  </div>

  <div class="abs news-thumb thumb-device" style="top:1584px" role="img" aria-label="Photograph of a piece of medical monitoring equipment"></div>
  <div class="abs news-item" style="top:1589px">
    <h3>Medical Equipment</h3>
    <div class="meta">September 15, 2013 &nbsp; <b>Comments (2)</b></div>
    <p>Cum sociis natoque penatibus et magnis dis parturient montesmus. Pro vel nibh et elit mollis commodo et nec augueique Mauris at justo eu lectus auctor porta vel ut libero.</p>
  </div>

  <h2 class="abs section-title" style="left:621px">Testimonials</h2>
  <div class="abs section-rule" style="left:621px;width:522px"></div>
  <div class="abs pager" style="left:1095px;top:1357px">
    <span><svg width="6" height="9" viewBox="0 0 6 9"><path d="M5 1L1 4.5 5 8" fill="none" stroke="#aaa" stroke-width="1.5"/></svg></span>
    <span class="on"><svg width="6" height="9" viewBox="0 0 6 9"><path d="M1 1l4 3.5L1 8" fill="none" stroke="#fff" stroke-width="1.5"/></svg></span>
  </div>

  <div class="abs quote-box"></div>
  <div class="abs qmark" style="left:640px;top:1468px">“</div>
  <p class="abs quote-text">Cum sociis natoque penatibus et magnis dis parturient esmus. Pro vel nibh et elit mollis commodo et nec augueique Mauris at justo eu lectus auctor porta vel ut libero. Suspe mattis tellus vel augue mollis ultrices. Suspendisse poten.</p>
  <div class="abs qmark" style="left:936px;top:1552px">”</div>
  <div class="abs avatar" role="img" aria-label="Portrait photograph of the reviewer"></div>
  <div class="abs person"><b>Dana Whitlock</b><span>Our Psychologist</span></div>
</section>

<section class="abs strip">
  <span class="strip-mark"></span>
  <p>Cum sociis natoque penatibus et magnis dis parturient montesmus. Pro vel nibh et elit mollis commodo et nec augueique Mauris at justo eu lectus</p>
  <div class="pager">
    <span><svg width="6" height="9" viewBox="0 0 6 9"><path d="M5 1L1 4.5 5 8" fill="none" stroke="#fff" stroke-width="1.5"/></svg></span>
    <span><svg width="6" height="9" viewBox="0 0 6 9"><path d="M1 1l4 3.5L1 8" fill="none" stroke="#fff" stroke-width="1.5"/></svg></span>
  </div>
</section>

<footer>
  <div class="abs footer"></div>

  <div class="abs fcol" style="left:57px;width:240px">
    <h4>Veridane Works.inc</h4>
    <p style="margin-top:36px">Cum sociis natoque penatibus et magnis dis parturient montesmus. Pro vel nibh et elit mollis commodo et nec augueque</p>
    <div class="finfo" style="margin-top:40px"><svg width="12" height="16" viewBox="0 0 12 16"><path d="M6 0a6 6 0 0 0-6 6c0 4 6 10 6 10s6-6 6-10a6 6 0 0 0-6-6zm0 8.5a2.5 2.5 0 1 1 0-5 2.5 2.5 0 0 1 0 5z"/></svg><span>Veridane Works.inc<br>Street Name 123<br>123 45 Cityname</span></div>
    <div class="finfo"><svg width="12" height="16" viewBox="0 0 12 16"><rect x="1" width="10" height="16" rx="2"/></svg><span>+123 900 555 010</span></div>
    <div class="finfo" style="margin-top:16px"><svg width="14" height="11" viewBox="0 0 14 11"><rect width="14" height="11" rx="1"/></svg><span>info@veridane.example</span></div>
  </div>

  <div class="abs fcol" style="left:338px;width:243px">
    <h4>Services</h4>
    <p style="margin-top:238px;color:#fff;font-size:13px">Accurate analyzes</p>
    <p style="margin-top:10px">Cum sociis natoque penatibus et magnis dis parturient montesmus. Pro vel nibh et elit</p>
  </div>
  <div class="abs pager" style="left:539px;top:1873px">
    <span style="border-color:#555"><svg width="6" height="9" viewBox="0 0 6 9"><path d="M5 1L1 4.5 5 8" fill="none" stroke="#888" stroke-width="1.5"/></svg></span>
    <span style="background:#fff;border-color:#fff"><svg width="6" height="9" viewBox="0 0 6 9"><path d="M1 1l4 3.5L1 8" fill="none" stroke="#333" stroke-width="1.5"/></svg></span>
  </div>
  <div class="abs footer-photo" role="img" aria-label="Photograph of a smiling doctor in a white coat with colleagues behind"></div>

  <div class="abs fcol" style="left:621px;width:240px">
    <h4>Doctors</h4>
    <ul>
      <li>Careers</li><li>Company news</li><li>Investor relations</li><li>Site map</li>
      <li>Community</li><li>Gallery</li><li>Updates</li><li>Videos</li>
    </ul>
  </div>

  <div class="abs fcol" style="left:900px;width:243px">
    <h4>Quick Contacts</h4>
    <div class="field-label" style="margin-top:26px">Your Email</div>
    <div class="field" style="height:33px"></div>
    <div class="field-label">Your Email</div>
    <div class="field" style="height:103px"></div>
    <div class="btn">Submit</div>
  </div>

  <div class="abs footer-base">VERIDANE WORKS.INC © 2014 All rights reserved</div>
</footer>

</body>
</html>
```